GHollis Busisness Card

I am an aerospace consultant and at this time only need business cards.

Industry/Entity Type

Business

Contact Information for Business Card

Hollis Partners,LLC
Gerald T. Hollis

348 Birch Hollow Road
Madison AL 35762

256-555-0148 (cell)
256-555-0173 (fax)

geraldhollis@mailbrook.net

```html
<!DOCTYPE html>
<html lang="en">
<head>
<meta charset="utf-8">
<title>Hollis Partners – Business Card</title>
<link rel="stylesheet" href="https://fonts.googleapis.com/css2?family=Cinzel:wght@500;600&family=Lato:wght@400;700&display=swap">
<style>
  :root {
    --backdrop: #2b2b2b;
    --card: #ffffff;
    --navy: #2b2a7c;
    --red: #d21f2b;
  }
  html, body {
    margin: 0;
    width: 1200px;
    height: 1000px;
    overflow: hidden;
    background: var(--backdrop);
  }
  .business-card {
    position: absolute;
    left: 145px;
    top: 240px;
    width: 910px;
    height: 520px;
    background: var(--card);
    overflow: hidden;
    box-shadow: 0 20px 40px rgba(0,0,0,0.5);
  }
  .brand {
    position: absolute;
    left: 0;
    right: 0;
    top: 90px;
    display: flex;
    align-items: center;
    justify-content: center;
    gap: 18px;
  }
  .brand-mark {
    width: 22px;
    height: 22px;
    border-radius: 50%;
    background: var(--red);
  }
  .brand-name {
    font-family: "Cinzel", serif;
    font-weight: 600;
    font-size: 52px;
    letter-spacing: 1px;
    color: var(--navy);
  }
  .holder {
    position: absolute;
    left: 0;
    right: 0;
    top: 215px;
    text-align: center;
  }
  .holder-name {
    font-family: "Cinzel", serif;
    font-weight: 500;
    font-size: 30px;
    color: var(--red);
    line-height: 1.1;
  }
  .holder-title {
    font-family: "Lato", sans-serif;
    font-size: 20px;
    color: var(--navy);
  }
  .office {
    position: absolute;
    right: 60px;
    top: 300px;
    font-family: "Lato", sans-serif;
    font-size: 21px;
    color: var(--navy);
    line-height: 1.25;
  }
  .office-company {
    font-weight: 700;
    font-size: 19px;
    color: var(--red);
  }
  .contacts {
    position: absolute;
    left: 50px;
    bottom: 60px;
    list-style: none;
    margin: 0;
    padding: 0;
    font-family: "Lato", sans-serif;
    font-size: 22px;
    color: var(--navy);
  }
  .contacts li {
    display: flex;
    align-items: center;
    gap: 14px;
    line-height: 1.35;
  }
  .contacts svg {
    width: 20px;
    height: 20px;
    fill: var(--red);
  }
  .footer-band {
    position: absolute;
    left: 0;
    bottom: 0;
    width: 910px;
    height: 26px;
  }
</style>
</head>
<body>
  <div class="business-card">
    <div class="brand">
      <span class="brand-mark"></span>
      <span class="brand-name">HOLLIS PARTNERS</span>
    </div>

    <div class="holder">
      <div class="holder-name">Gerald T. Hollis</div>
      <div class="holder-title">Aerospace Consultant</div>
    </div>

    <div class="office">
      <div class="office-company">HOLLIS PARTNERS, LLC</div>
      <div>348 Birch Hollow Road</div>
      <div>Madison AL 35762</div>
    </div>

    <ul class="contacts">
      <li>
        <svg viewBox="0 0 20 20" aria-hidden="true"><path d="M6 1h8a1.5 1.5 0 0 1 1.5 1.5v15A1.5 1.5 0 0 1 14 19H6a1.5 1.5 0 0 1-1.5-1.5v-15A1.5 1.5 0 0 1 6 1zm0 2v12h8V3zm4 13a1 1 0 1 0 0 2 1 1 0 0 0 0-2z"/></svg>
        256-555-0148
      </li>
      <li>
        <svg viewBox="0 0 20 20" aria-hidden="true"><path d="M5 1h10v5H5zM2 7h16a1 1 0 0 1 1 1v7h-3v4H4v-4H1V8a1 1 0 0 1 1-1zm4 6v4h8v-4z"/></svg>
        256-555-0173
      </li>
      <li>
        <svg viewBox="0 0 20 20" aria-hidden="true"><path d="M1 4h18v2l-9 6-9-6zm0 4 9 6 9-6v8H1z"/></svg>
        geraldhollis@mailbrook.net
      </li>
    </ul>

    <svg class="footer-band" viewBox="0 0 910 26" preserveAspectRatio="none" aria-hidden="true">
      <polygon points="0,0 470,0 450,26 0,26" fill="var(--red)"/>
      <polygon points="470,0 910,0 910,26 450,26" fill="var(--navy)"/>
    </svg>
  </div>
</body>
</html>
```